Tilda Tinkerwire, An IT Company Has New Logo, Need Fresh Business Cards

IT company is called Tilda Tinkerwire and is displayed nicely with the new logo from here on pitchloft. Would like a fresh business card look that encompasses the idea that we want clients to Cherish Every Gadget. I love the use of circuitry with hearts as endpoints and x's and o's. It needs to have room for my certification logos of which there are 4 and a BRJ Alumni log. I am attaching my current card to illustrate how it has always captured attention, but that was in the early stages of business when I was doing more residential work. I am focused on businesses now, so a level of professionalism is necessary. I would also like the card to lend itself well to additional stationary, email signature, ticketing template for my workboard, etc. For the time being, I need the card for an upcoming conference so that work will come later. Color scheme should be that of the new logo. Thank you and I look forward to the designs.

Target Market(s)

Businesses looking for IT services.

Industry/Entity Type

Information Technology

Contact Information for Business Card

See above

Requirements
Must have
• New logo colors and a warm feel. Possibly a tad feminine as I am female, but appealing to males.
Nice to have
• I would like techy, but no too much so. I like friendly and connecting feels. People LOVED my old card and called me because it gave them a warm feeling.

```html
<!DOCTYPE html>
<html lang="en">
<head>
<meta charset="utf-8">
<title>Tilda Tinkerwire – Business Card</title>
<link href="https://fonts.googleapis.com/css2?family=Questrial&family=Montserrat:wght@400;600&family=Oswald:wght@500&display=swap" rel="stylesheet">
<style>
  :root{
    --bg:#e8e5e1;
    --card:#ffffff;
    --pink:#eea5c9;
    --blue:#86cbe8;
    --green:#c3dc7a;
    --ink:#2f2f33;
    --strip:#333438;
    --rule:#bdbdbd;
    --badge-a:#b8cde6;
    --badge-b:#cfd3d9;
    --gold:#f2c13a;
  }
  *{margin:0;padding:0;box-sizing:border-box}
  html,body{width:1200px;height:1134px;overflow:hidden;background:var(--bg)}
  .canvas{position:relative;width:1200px;height:1134px}
  .card{position:absolute;left:234px;width:680px;height:406px;background:var(--card);
    box-shadow:0 14px 28px rgba(0,0,0,.22);overflow:hidden}
  .card--front{top:90px}
  .card--back{top:625px}

  /* brand block */
  .brand{position:absolute;text-align:center;font-family:"Questrial",sans-serif}
  .brand__dot{display:block;border-radius:50%;background:var(--pink);margin:0 auto}
  .brand__name{color:var(--blue);white-space:nowrap}
  .brand__tagline{color:var(--pink);font-family:"Montserrat",sans-serif;font-weight:600;
    letter-spacing:.18em;text-transform:uppercase;white-space:nowrap}

  .front-brand{left:21px;top:72px;width:220px}
  .front-brand .brand__dot{width:40px;height:40px;margin-bottom:14px}
  .front-brand .brand__name{font-size:22px;line-height:26px}
  .front-brand .brand__tagline{font-size:6.5px;margin-top:2px}

  .back-brand{left:192px;top:132px;width:440px}
  .back-brand .brand__dot{width:60px;height:60px;margin-bottom:28px}
  .back-brand .brand__name{font-size:36px;line-height:44px}
  .back-brand .brand__tagline{font-size:9.5px;margin-top:3px}

  /* credentials */
  .credentials{position:absolute;top:168px;left:0;width:100%;height:40px}
  .badge{position:absolute;top:0;height:32px;border-radius:4px}
  .badge--cert-a{left:328px;width:100px;background:var(--badge-a)}
  .badge--cert-b{left:454px;width:62px;background:var(--badge-b)}
  .alumni{position:absolute;left:547px;top:0;width:120px;height:36px;border-bottom:1px solid var(--rule);
    display:flex;align-items:center;gap:10px;font-family:"Montserrat",sans-serif;font-size:13px;
    font-weight:600;color:var(--ink);white-space:nowrap}
  .alumni__mark{width:18px;height:18px;border-radius:50%;background:var(--gold);flex:none}

  /* band + contact */
  .front-band{position:absolute;left:0;top:0;width:680px;height:406px}
  .contact{position:absolute;left:116px;top:296px;list-style:none;font-family:"Montserrat",sans-serif;
    font-size:14.5px;color:#fff;line-height:22px;white-space:nowrap}
  .services{position:absolute;left:431px;top:290px;font-family:"Oswald",sans-serif;font-weight:500;
    font-size:20px;line-height:34px;color:#fff;text-transform:uppercase;white-space:nowrap}

  .back-art{position:absolute;left:0;top:0}
</style>
</head>
<body>
<main class="canvas">

  <section class="card card--front" aria-label="Business card front">
    <svg class="front-band" viewBox="0 0 680 406" aria-hidden="true">
      <path d="M0 212 H87 L99 228 L111 212 H680 V406 H0 Z" fill="var(--pink)"/>
      <path d="M99 228 V406" stroke="#fff" stroke-width="3"/>
      <rect x="82" y="281" width="29" height="94" fill="var(--strip)"/>
      <path d="M93.5 301.5 q0 8.5 8.5 8.5" fill="none" stroke="#fff" stroke-width="3" stroke-linecap="round"/>
      <rect x="92" y="321" width="10" height="7" fill="#fff"/>
      <circle cx="97" cy="351" r="5" fill="none" stroke="#fff" stroke-width="1.3"/>
      <path d="M92 351h10M97 346v10" stroke="#fff" stroke-width="1"/>
    </svg>

    <div class="brand front-brand">
      <span class="brand__dot"></span>
      <div class="brand__name">Tilda Tinkerwire</div>
      <div class="brand__tagline">Cherish Every Gadget</div>
    </div>

    <div class="credentials">
      <div class="badge badge--cert-a" role="img" aria-label="Certification badge"></div>
      <div class="badge badge--cert-b" role="img" aria-label="Certification badge"></div>
      <div class="alumni"><span class="alumni__mark"></span>BRJ Alumni</div>
    </div>

    <ul class="contact">
      <li>407-555-0182</li>
      <li>tilda.tinkerwire@mailbox.com</li>
      <li>www.tilda-tinkerwire.com</li>
    </ul>

    <p class="services">Computer Care &amp; Repair<br>Desktops, Laptop, Tablets</p>
  </section>

  <section class="card card--back" aria-label="Business card back">
    <svg class="back-art" width="680" height="406" viewBox="0 0 680 406" aria-hidden="true">
      <path d="M0 0 H163 V50 L204 85 L163 121 V406 H0 Z" fill="var(--blue)"/>
    </svg>
    <div class="brand back-brand">
      <span class="brand__dot"></span>
      <div class="brand__name">Tilda Tinkerwire</div>
      <div class="brand__tagline">Cherish Every Gadget</div>
    </div>
  </section>

</main>
</body>
</html>
```